Redesign Colorful Business Card

Please redesign the card attached. It is too busy. Please don't eliminate any of the words. The repetivite word "free" can be used less often.

Target Market(s)

College Students.

Contact Information for Business Card

The details listed in the attached image

Font styles to use
Sans Serif

Requirements
Must have
• A clear and simple presentation and must be attractive.

```html
<!DOCTYPE html>
<html lang="en">
<head>
<meta charset="utf-8">
<title>StudyEZ Business Card</title>
<link href="https://fonts.googleapis.com/css2?family=Poppins:wght@400;600;700;800&display=swap" rel="stylesheet">
<style>
  :root{
    --bg:#1b1d33;
    --brand-blue:#2446a8;
    --sky:#c7e8f7;
    --ink:#14141c;
    --white:#ffffff;
    --ribbon:#d81f26;
    --ribbon-dark:#9e1419;
    --rule-pink:#b957b6;
    --rule-green:#5cbf4a;
    --s1:#5db6c7;--s2:#2f4ea6;--s3:#f0dc96;--s4:#1a1a1a;--s5:#7a4a6a;
    --s6:#b05aa8;--s7:#5cbf4a;--s8:#e52428;--s9:#dcd8cc;--s10:#d9a33a;
  }
  html,body{margin:0;padding:0;width:1200px;height:1200px;overflow:hidden;background:var(--bg);}
  body{display:flex;align-items:center;justify-content:center;font-family:'Poppins',sans-serif;}
  .card{position:relative;width:1080px;height:620px;background:var(--sky);overflow:hidden;box-shadow:0 20px 50px rgba(0,0,0,.5);}
  .band-top{position:absolute;left:0;top:0;width:100%;height:168px;background:var(--brand-blue);}
  .band-bottom{position:absolute;left:0;bottom:26px;width:100%;height:148px;background:var(--brand-blue);}
  .stripes{position:absolute;left:0;bottom:0;width:100%;height:26px;display:flex;}
  .stripes span{flex:1;}
  .brand{position:absolute;left:420px;top:48px;display:flex;align-items:center;gap:18px;color:var(--white);font-size:46px;font-weight:600;letter-spacing:.5px;}
  .brand-mark{width:54px;height:54px;border-radius:50%;background:var(--white);}
  .ribbon{position:absolute;left:40px;top:92px;width:300px;height:260px;}
  .benefits{position:absolute;left:300px;top:210px;margin:0;padding:0;list-style:none;}
  .benefit{display:flex;align-items:center;gap:22px;font-size:27px;font-weight:700;color:var(--ink);text-transform:uppercase;padding:12px 0;}
  .benefit + .benefit{border-top:3px solid var(--rule-pink);}
  .benefit:nth-child(3){border-top-color:var(--rule-green);}
  .benefit svg{width:40px;height:40px;flex:none;}
  .contact{position:absolute;left:0;right:0;bottom:94px;text-align:center;color:var(--white);font-size:25px;font-weight:400;}
  .contact b{font-weight:700;}
  .copyright{position:absolute;left:0;right:0;bottom:50px;text-align:center;color:var(--white);font-size:18px;}
</style>
</head>
<body>
  <div class="card">
    <div class="band-top"></div>
    <div class="brand"><span class="brand-mark"></span>StudyEZ.com</div>

    <svg class="ribbon" viewBox="0 0 300 260" aria-hidden="true">
      <polygon points="60,150 120,150 150,260 90,200" fill="var(--ribbon-dark)"/>
      <polygon points="0,90 240,0 300,60 60,170" fill="var(--ribbon)"/>
      <text x="150" y="110" transform="rotate(-21 150 90)" text-anchor="middle" font-family="Poppins, sans-serif" font-weight="800" font-size="72" fill="#fff">FREE</text>
    </svg>

    <ul class="benefits">
      <li class="benefit">
        <svg viewBox="0 0 40 40" fill="none" stroke="#d81f26" stroke-width="2.5"><circle cx="20" cy="23" r="13"/><path d="M16 5h8M20 5v5M20 23l5-5"/></svg>
        Cut study time down by up to 50%
      </li>
      <li class="benefit">
        <svg viewBox="0 0 40 40" fill="none" stroke="#5a5a6a" stroke-width="2.5"><rect x="6" y="8" width="28" height="19" rx="2"/><path d="M2 32h36"/></svg>
        Learn a subject without having to go to class
      </li>
      <li class="benefit">
        <svg viewBox="0 0 40 40" fill="none" stroke="#d9a33a" stroke-width="2.5"><path d="M20 5a11 11 0 0 0-6 20v5h12v-5a11 11 0 0 0-6-20z"/><path d="M15 35h10"/></svg>
        Memorize anything quickly
      </li>
    </ul>

    <div class="band-bottom"></div>
    <div class="contact"><b>W:</b> www.studyez.com | <b>E:</b> info@studyez.com | <b>C:</b> 98700 12345</div>
    <div class="copyright">Copyright EZ Learning Services, LLC 2013-2022 All Rights Reserved</div>

    <div class="stripes">
      <span style="background:var(--s1)"></span><span style="background:var(--s2)"></span>
      <span style="background:var(--s3)"></span><span style="background:var(--s4)"></span>
      <span style="background:var(--s5)"></span><span style="background:var(--s6)"></span>
      <span style="background:var(--s7)"></span><span style="background:var(--s8)"></span>
      <span style="background:var(--s9)"></span><span style="background:var(--s10)"></span>
    </div>
  </div>
</body>
</html>
```